New business card for civil engineering company - "Keystone Audit"

We need a business card designed for our new structural engineering company.

The company name is "Keystone Audit" logo files attached.

We would like the following:
* Two-sided card
* Simple design

Information to be placed on the card:
Name - Marcus Dellow
Job Title - Director / Structural Engineer
Credentials - BEng(Hons), CPEng, CMengNZ, IntPE(NZ)
Email - marcus.dellow@keystoneaudit.co.nz
mobile - 0219364058
website - www.keystoneaudit.co.nz

```html
<!DOCTYPE html>
<html lang="en">
<head>
<meta charset="UTF-8">
<title>Keystone Audit – Business Card</title>
<link rel="stylesheet" href="https://fonts.googleapis.com/css2?family=Open+Sans:wght@400;600;700&display=swap">
<style>
  :root {
    --stage: #3a3a3c;
    --card-dark: #231f20;
    --card-light: #ffffff;
    --facet-light: #f4f4f5;
    --facet-mid: #e6e6e8;
    --brand-blue: #1a73c2;
    --rule-blue: #8fd0ec;
    --ink: #2b2b2b;
    --ink-soft: #4a4a4a;
    --white: #ffffff;
  }
  * { box-sizing: border-box; margin: 0; padding: 0; }
  html, body {
    width: 1200px; height: 900px; overflow: hidden;
    background: var(--stage);
    font-family: "Open Sans", Arial, sans-serif;
  }
  .canvas {
    position: relative; width: 1200px; height: 900px;
  }
  .card {
    position: absolute; left: 285px;
    width: 630px; height: 360px;
    border-radius: 22px;
    overflow: hidden;
    box-shadow: 0 18px 40px rgba(0,0,0,.45);
  }
  /* Back */
  .card-back {
    top: 50px;
    background: var(--card-dark);
    display: flex; flex-direction: column;
    align-items: center; justify-content: center;
  }
  .brand {
    display: flex; align-items: center; gap: 14px;
  }
  .brand-mark {
    width: 22px; height: 22px; background: var(--brand-blue);
  }
  .brand-name {
    font-weight: 600; letter-spacing: 4px; text-transform: uppercase;
  }
  .card-back .brand-name { color: var(--white); font-size: 34px; }
  .tagline {
    text-transform: uppercase; letter-spacing: 4px;
  }
  .card-back .tagline {
    color: var(--white); font-size: 12px; margin-top: 10px;
  }
  /* Front */
  .card-front {
    top: 440px;
    background: var(--card-light);
  }
  .facet-field {
    position: absolute; inset: 0;
    background: linear-gradient(125deg, var(--facet-mid) 0%, var(--facet-light) 35%, var(--card-light) 55%, var(--facet-light) 75%, var(--facet-mid) 100%);
  }
  .front-brand {
    position: absolute; left: 38px; top: 44px;
  }
  .card-front .brand-name { color: var(--ink); font-size: 24px; letter-spacing: 3px; }
  .card-front .brand-mark { width: 16px; height: 16px; }
  .card-front .tagline {
    color: var(--ink); font-size: 9px; margin-top: 6px; letter-spacing: 2.6px;
  }
  .person {
    position: absolute; right: 38px; top: 118px; text-align: right;
  }
  .person-name {
    color: var(--brand-blue); font-weight: 700; font-size: 30px; line-height: 1.1;
  }
  .person-role {
    color: var(--ink-soft); font-size: 15px; margin-top: 6px;
  }
  .person-credentials {
    color: var(--ink-soft); font-size: 15px; margin-top: 4px;
  }
  .divider {
    position: absolute; left: 38px; right: 38px; top: 232px;
    height: 1px; background: var(--rule-blue);
  }
  .contacts {
    position: absolute; left: 38px; top: 250px;
    list-style: none;
  }
  .contacts li {
    display: flex; align-items: center; gap: 10px;
    color: var(--ink); font-size: 15px; line-height: 28px;
  }
  .contacts svg { width: 15px; height: 15px; flex: none; }
</style>
</head>
<body>
<main class="canvas">
  <section class="card card-back" aria-label="Card back">
    <div class="brand">
      <span class="brand-mark"></span>
      <span class="brand-name">Keystone Audit</span>
    </div>
    <p class="tagline">Peer Review Specialists</p>
  </section>

  <section class="card card-front" aria-label="Card front">
    <div class="facet-field" role="img" aria-label="Soft grey low-poly faceted background"></div>
    <div class="front-brand">
      <div class="brand">
        <span class="brand-mark"></span>
        <span class="brand-name">Keystone Audit</span>
      </div>
      <p class="tagline">Peer Review Specialists</p>
    </div>

    <div class="person">
      <p class="person-name">Marcus Dellow</p>
      <p class="person-role">Director / Structural Engineer</p>
      <p class="person-credentials">BEng(Hons), CPEng, CMengNZ, IntPE(NZ)</p>
    </div>

    <div class="divider"></div>

    <ul class="contacts">
      <li>
        <svg viewBox="0 0 24 24" aria-hidden="true"><path fill="var(--brand-blue)" d="M6.6 10.8a15.1 15.1 0 0 0 6.6 6.6l2.2-2.2a1 1 0 0 1 1-.25 11.4 11.4 0 0 0 3.6.57 1 1 0 0 1 1 1V20a1 1 0 0 1-1 1A17 17 0 0 1 3 4a1 1 0 0 1 1-1h3.5a1 1 0 0 1 1 1c0 1.25.2 2.45.57 3.57a1 1 0 0 1-.25 1z"/></svg>
        0219364058
      </li>
      <li>
        <svg viewBox="0 0 24 24" aria-hidden="true"><rect x="2" y="5" width="20" height="14" rx="1.5" fill="var(--brand-blue)"/><path d="M3 6.5l9 6.5 9-6.5" fill="none" stroke="var(--white)" stroke-width="1.8"/></svg>
        marcus.dellow@keystoneaudit.co.nz
      </li>
      <li>
        <svg viewBox="0 0 24 24" aria-hidden="true"><circle cx="12" cy="12" r="10" fill="var(--brand-blue)"/><path d="M2 12h20M12 2c3 3 3 17 0 20M12 2c-3 3-3 17 0 20" fill="none" stroke="var(--white)" stroke-width="1.4"/></svg>
        www.keystoneaudit.co.nz
      </li>
    </ul>
  </section>
</main>
</body>
</html>
```